Building Maintenance Company Capability Statement

We would like a capability statement designed please.

Let us know where we can supply the written text.

Ideally, most of the information will be on our website.
www.tidewellgroup.com.au

Target Market(s)

Strata and building managers. schools and educational facilities, retirement and aged care.

Industry/Entity Type

Building

Font styles to use
Other font styles liked:
• nanito sans light

Requirements
Must have
• Images of people working (we can supply)
Easy to skim read
Colourful and attractive
Should not have
• lots of words

```html
<!DOCTYPE html>
<html lang="en">
<head>
<meta charset="utf-8">
<title>Tidewell Maintenance Group – Capability Flyer</title>
<link href="https://fonts.googleapis.com/css2?family=Oswald:wght@500;600&family=Montserrat:wght@400;600;700&display=swap" rel="stylesheet">
<style>
  :root{
    --paper:#f4f5f7;
    --navy:#2c5a84;
    --blue:#3f7fb8;
    --sky:#8cc4e8;
    --bright:#2b98d6;
    --red:#d43d4f;
    --grey:#7b7b7d;
    --panel-top:#3c6d98;
    --panel-bottom:#5f8db5;
    --white:#ffffff;
  }
  *{box-sizing:border-box;margin:0;padding:0}
  html,body{width:1165px;height:1200px;overflow:hidden;background:var(--paper)}
  .flyer{position:relative;width:1165px;height:1200px;background:var(--paper);font-family:'Montserrat',sans-serif;overflow:hidden}
  .hero{position:absolute;left:0;top:0;width:1165px;height:760px}

  .tag{position:absolute;height:54px;display:flex;align-items:center;justify-content:center;
       font-family:'Oswald',sans-serif;font-weight:600;font-size:30px;letter-spacing:3px;color:var(--white);
       border-radius:10px;transform:skewX(-12deg)}
  .tag span{transform:skewX(12deg)}
  .tag--trusted{left:170px;top:690px;width:270px;background:var(--red)}
  .tag--reliable{left:455px;top:742px;width:270px;background:var(--blue)}
  .tag--experienced{left:745px;top:794px;width:290px;background:var(--grey)}

  .tag-rule{position:absolute;height:4px;background:var(--navy);border-radius:2px}
  .tag-rule--lead{left:120px;top:714px;width:44px}
  .tag-rule--tail{left:1042px;top:818px;width:90px}

  .headline{position:absolute;left:58px;top:770px;font-family:'Oswald',sans-serif;font-weight:500;font-size:50px;line-height:56px}
  .headline .muted{color:var(--grey)}
  .headline .accent{color:var(--red)}
  .headline .cool{color:var(--bright)}
  .headline-rule{position:absolute;left:62px;top:1062px;width:48px;height:6px;background:var(--red);border-radius:3px}

  .brand{position:absolute;left:60px;top:1094px;display:flex;align-items:center;gap:12px}
  .brand-dot{width:30px;height:30px;border-radius:50%;background:var(--navy)}
  .brand-name{font-family:'Montserrat',sans-serif;font-weight:700;font-size:22px;color:var(--navy)}
  .email{position:absolute;left:60px;top:1140px;display:flex;align-items:center;gap:10px;font-size:18px;color:var(--navy)}

  .services-rule{position:absolute;left:430px;top:812px;width:300px;height:18px}
  .services-title{position:absolute;left:640px;top:850px;font-family:'Oswald',sans-serif;font-weight:600;font-size:30px;line-height:40px;letter-spacing:2px;color:var(--bright)}
  .services{position:absolute;left:430px;top:896px;width:680px;height:190px;border-radius:30px;
            background:linear-gradient(160deg,var(--panel-top),var(--panel-bottom));
            display:grid;grid-template-columns:1fr 1fr;column-gap:30px;padding:12px 40px}
  .services ul{list-style:none;display:flex;flex-direction:column;gap:10px}
  .services li{display:flex;align-items:flex-start;gap:10px;color:var(--white);font-size:17px;line-height:21px}
  .services li svg{flex:none;margin-top:2px}

  .contact{position:absolute;right:70px;top:1098px;text-align:right}
  .contact-label{font-size:24px;letter-spacing:2px;color:var(--navy);display:flex;align-items:center;justify-content:flex-end;gap:10px}
  .contact-phone{font-size:46px;font-weight:700;color:var(--red);line-height:50px}
  .base-band{position:absolute;left:0;bottom:0;width:1165px;height:14px;background:var(--navy)}
</style>
</head>
<body>
<main class="flyer">
  <svg class="hero" viewBox="0 0 1165 760">
    <defs>
      <linearGradient id="photoMain" x1="0" y1="0" x2="1" y2="1">
        <stop offset="0" stop-color="#cfcfcc"/>
        <stop offset=".45" stop-color="#c9cf6a"/>
        <stop offset="1" stop-color="#8a8378"/>
      </linearGradient>
      <linearGradient id="photoInset" x1="0" y1="0" x2="1" y2="1">
        <stop offset="0" stop-color="#56708f"/>
        <stop offset=".5" stop-color="#e6e2d6"/>
        <stop offset="1" stop-color="#d9d4c4"/>
      </linearGradient>
    </defs>
    <circle class="swoosh-navy" cx="740" cy="60" r="690" fill="#2c5a84"/>
    <circle class="swoosh-blue" cx="730" cy="60" r="650" fill="#3f7fb8"/>
    <circle class="swoosh-sky" cx="720" cy="60" r="625" fill="#8cc4e8"/>
    <circle class="swoosh-bright" cx="715" cy="60" r="612" fill="#2b98d6"/>
    <circle class="photo-main" cx="712" cy="60" r="598" fill="url(#photoMain)" role="img" aria-label="Photo: maintenance worker in hi-vis shirt using a nail gun on a timber fence"/>
    <circle class="photo-inset" cx="975" cy="320" r="230" fill="url(#photoInset)" stroke="#ffffff" stroke-width="7" role="img" aria-label="Photo: rope access technician pressure washing a building facade"/>
  </svg>

  <div class="tag-rule tag-rule--lead"></div>
  <div class="tag tag--trusted"><span>TRUSTED</span></div>
  <div class="tag tag--reliable"><span>RELIABLE</span></div>
  <div class="tag tag--experienced"><span>EXPERIENCED</span></div>
  <div class="tag-rule tag-rule--tail"></div>

  <h1 class="headline">
    <span class="muted">We Provide</span><br>
    <span class="accent">Cost Effective</span><br>
    <span class="accent">Solutions</span> <span class="muted">To Your</span><br>
    <span class="cool">Building And</span><br>
    <span class="cool">Maintainance</span>
  </h1>
  <div class="headline-rule"></div>

  <div class="brand"><span class="brand-dot"></span><span class="brand-name">TIDEWELL MAINTENANCE GROUP</span></div>
  <div class="email">
    <svg width="24" height="18" viewBox="0 0 24 18"><rect x="1" y="1" width="22" height="16" rx="2" fill="none" stroke="#2c5a84" stroke-width="2"/><path d="M1 2 L12 10 L23 2" fill="none" stroke="#2c5a84" stroke-width="2"/></svg>
    hello@tidewellgroup.com.au
  </div>

  <svg class="services-rule" viewBox="0 0 300 18"><path d="M4 4 H296" stroke="#2c5a84" stroke-width="5" stroke-linecap="round"/><path d="M4 13 H296" stroke="#3f7fb8" stroke-width="3" stroke-linecap="round"/></svg>
  <h2 class="services-title">OUR SERVICES</h2>

  <section class="services">
    <ul>
      <li><svg width="18" height="18" viewBox="0 0 18 18"><circle cx="9" cy="9" r="8" fill="none" stroke="#cfe3f3" stroke-width="1.5"/><path d="M5 9 L8 12 L13 6" fill="none" stroke="#cfe3f3" stroke-width="1.8"/></svg>Internal and External Painting Works</li>
      <li><svg width="18" height="18" viewBox="0 0 18 18"><circle cx="9" cy="9" r="8" fill="none" stroke="#cfe3f3" stroke-width="1.5"/><path d="M5 9 L8 12 L13 6" fill="none" stroke="#cfe3f3" stroke-width="1.8"/></svg>Electrical</li>
      <li><svg width="18" height="18" viewBox="0 0 18 18"><circle cx="9" cy="9" r="8" fill="none" stroke="#cfe3f3" stroke-width="1.5"/><path d="M5 9 L8 12 L13 6" fill="none" stroke="#cfe3f3" stroke-width="1.8"/></svg>Plumbing</li>
      <li><svg width="18" height="18" viewBox="0 0 18 18"><circle cx="9" cy="9" r="8" fill="none" stroke="#cfe3f3" stroke-width="1.5"/><path d="M5 9 L8 12 L13 6" fill="none" stroke="#cfe3f3" stroke-width="1.8"/></svg>Roofing</li>
    </ul>
    <ul>
      <li><svg width="18" height="18" viewBox="0 0 18 18"><circle cx="9" cy="9" r="8" fill="none" stroke="#cfe3f3" stroke-width="1.5"/><path d="M5 9 L8 12 L13 6" fill="none" stroke="#cfe3f3" stroke-width="1.8"/></svg>Plastering</li>
      <li><svg width="18" height="18" viewBox="0 0 18 18"><circle cx="9" cy="9" r="8" fill="none" stroke="#cfe3f3" stroke-width="1.5"/><path d="M5 9 L8 12 L13 6" fill="none" stroke="#cfe3f3" stroke-width="1.8"/></svg>Carpentry and Repairs</li>
      <li><svg width="18" height="18" viewBox="0 0 18 18"><circle cx="9" cy="9" r="8" fill="none" stroke="#cfe3f3" stroke-width="1.5"/><path d="M5 9 L8 12 L13 6" fill="none" stroke="#cfe3f3" stroke-width="1.8"/></svg>AC Installations</li>
      <li><svg width="18" height="18" viewBox="0 0 18 18"><circle cx="9" cy="9" r="8" fill="none" stroke="#cfe3f3" stroke-width="1.5"/><path d="M5 9 L8 12 L13 6" fill="none" stroke="#cfe3f3" stroke-width="1.8"/></svg>Landscaping</li>
    </ul>
  </section>

  <div class="contact">
    <div class="contact-label">CONTACT US
      <svg width="28" height="24" viewBox="0 0 28 24"><path d="M2 3 Q2 1 4 1 H16 Q18 1 18 3 V11 Q18 13 16 13 H8 L4 17 V13 Q2 13 2 11 Z" fill="#2c5a84"/><path d="M20 7 H24 Q26 7 26 9 V17 Q26 19 24 19 V23 L20 19 H12 Q10 19 10 17 V15 H17 Q20 15 20 12 Z" fill="#2b98d6"/></svg>
    </div>
    <div class="contact-phone">(08) 9000 4821</div>
  </div>

  <div class="base-band"></div>
</main>
</body>
</html>
```